Buch-/E-Book-Cover für Sammlung von positiven Erfahrungen
Zielgruppe
die Zielgruppe sind Väter die ihren Söhne eine Sammlung von Empfehlungen für ein positives Leben schenken sollen. Der Titel des Buches heisst 'Zwischen Ebbe und Glut'
Aufgabenstellung
ich möchte mich hier von den Designern überraschen und inspirieren lassen.

```html
<!DOCTYPE html>
<html lang="de">
<head>
<meta charset="utf-8">
<title>Zwischen Ebbe und Glut – Cover</title>
<link rel="stylesheet" href="https://fonts.googleapis.com/css2?family=Anton&display=swap">
<style>
  :root {
    --page: #ffffff;
    --title-green: #04622a;
    --author-white: #ffffff;
    --sun-amber: #e9a848;
    --sun-yellow: #f7df5a;
    --sun-orange: #ea7420;
    --sun-deep: #b8461a;
  }
  html, body {
    margin: 0;
    padding: 0;
    width: 848px;
    height: 1200px;
    overflow: hidden;
    background: var(--page);
  }
  .canvas {
    position: relative;
    width: 848px;
    height: 1200px;
    background: var(--page);
  }
  .cover {
    position: absolute;
    left: 127px;
    top: 153px;
    width: 598px;
    height: 848px;
    overflow: hidden;
  }
  .cover-photo {
    position: absolute;
    inset: 0;
    background:
      radial-gradient(ellipse 55% 40% at 58% 72%, rgba(255,236,140,0.9), rgba(255,236,140,0) 70%),
      radial-gradient(ellipse 60% 45% at 35% 95%, var(--sun-deep), rgba(184,70,26,0) 70%),
      linear-gradient(100deg, var(--sun-amber) 0%, #f2c152 45%, var(--sun-yellow) 100%);
  }
  .cover-photo::after {
    content: "";
    position: absolute;
    inset: 0;
    background: linear-gradient(180deg, rgba(234,116,32,0) 55%, rgba(234,116,32,0.45) 100%);
  }
  .title {
    margin: 0;
    font-family: "Anton", "Impact", sans-serif;
    font-weight: 400;
    color: var(--title-green);
    text-transform: uppercase;
  }
  .title span {
    position: absolute;
    display: block;
    line-height: 1;
    white-space: nowrap;
  }
  .title-small-top { left: 34px;  top: 35px;  font-size: 61px; }
  .title-large-top { left: 42px;  top: 97px;  font-size: 153px; }
  .title-small-mid { left: 112px; top: 252px; font-size: 68px; }
  .title-large-bot { left: 244px; top: 247px; font-size: 153px; }
  .author {
    position: absolute;
    left: 157px;
    top: 791px;
    margin: 0;
    white-space: nowrap;
    font-family: "Anton", "Impact", sans-serif;
    font-weight: 400;
    font-size: 34px;
    line-height: 1;
    color: var(--author-white);
    text-transform: uppercase;
  }
</style>
</head>
<body>
  <div class="canvas">
    <section class="cover">
      <div class="cover-photo" role="img" aria-label="Silhouette eines Vaters, der seinen Sohn mit ausgebreiteten Armen auf den Schultern trägt, vor einem goldenen Sonnenuntergang am Meer"></div>
      <h1 class="title">
        <span class="title-small-top">Zwischen</span>
        <span class="title-large-top">Ebbe</span>
        <span class="title-small-mid">und</span>
        <span class="title-large-bot">Glut</span>
      </h1>
      <p class="author">Max Mustermann</p>
    </section>
  </div>
</body>
</html>
```